My company is for education support and is called Tallowbrook Classroom Services

21st Century Leading Teaching Learning is the tag line.

I am an education consultant in New York City. My company Tallowbrook Classroom Services is described by the words 21st Century Leading Teaching Learning. I need a website to house resources that schools can access as well as selling resources. I want to post photos of teaching situations. I want to connect to Chatterleaf, Quipline and a blog. I want drop down boxes.
I have just had my logo designed on Drawmarket.
Purpose of the website:
1. For teachers to build awareness of how to become more effective teachers
2. To support schools as they develop systems that improve schools
3. To want to have the ability to sell my knowledge and experience
Audience:
Educators
Teachers
Teacher teams
Leaders
Talent coaches
I have bought a domain and I have a business email.
I have just had a logo designed.
I will need an email address for the .eps file as I can't see how to attach to this message.
Tallowbrook Classroom Services is a company that offers professional development and support to schools. Through an analysis of each school’s needs; a knowledge of the national Harlow Academic Benchmarks; an alignment to the Varden Pedagogy Guidelines Initiative and Whitcombe’s Rubric for Classroom Practice, action plans are developed to support the principal’s vision, CEP and PPR that will translate into improved performance and progress for all students.Quality Professional Development and resources that support each school's needs. The company provides professional development to Educational Networks, Districts, Principals, Administration Teams, teachers and parents.

Here are some of my other thoughts:
Build in ability to sell
Choose the font carefully
Layout - allow for the download of big pics and pdfs
I don't want viewers to sign in
I do want them to register if they buy something

8 pages - home; about Tallowbrook; services; resources; media gallery; Contact Tallowbrook
I will answer any questions and discuss this project with you as much as you need. Better to pretalk my options than change things once they are set up.

Target Market(s)

Purpose of the website:

Industry/Entity Type

Education

Requirements
Must have
• 8 pages
Abilty to see from the site

```html
<!DOCTYPE html>
<html lang="en">
<head>
<meta charset="utf-8">
<title>Tallowbrook Classroom Services</title>
<link href="https://fonts.googleapis.com/css2?family=PT+Sans:wght@400;700&family=PT+Sans+Narrow:wght@400;700&display=swap" rel="stylesheet">
<style>
:root{
  --brand:#b5123b;
  --brand-dark:#9a0c2f;
  --brand-light:#c81e48;
  --ink:#333;
  --muted:#8a8a8a;
  --body:#555;
  --line:#ddd;
  --white:#fff;
}
*{box-sizing:border-box;margin:0;padding:0}
html,body{width:831px;height:1200px;overflow:hidden;background:var(--white)}
body{position:relative;font-family:"PT Sans",sans-serif;color:var(--ink)}
.abs{position:absolute}
a{color:inherit;text-decoration:none}

.utility{top:10px;right:83px;font-size:9px;color:var(--ink);display:flex;gap:5px;align-items:center}
.utility svg{width:14px;height:12px}

.brand{top:30px;left:84px;display:flex;align-items:center;gap:8px}
.brand-mark{width:28px;height:28px;border-radius:50%;background:var(--brand)}
.brand-name{font-size:19px;color:#555;letter-spacing:.6px;line-height:1}
.brand-tag{font-size:7px;color:#777;letter-spacing:.5px;margin-top:3px;border-top:1px solid #888;padding-top:2px;text-transform:uppercase}

.nav{top:76px;left:84px;width:665px;height:40px;background:linear-gradient(var(--brand-light),var(--brand-dark));display:flex;align-items:center}
.nav a{font-family:"PT Sans Narrow",sans-serif;font-weight:700;color:var(--white);font-size:12px;padding:0 19px;height:40px;line-height:40px;border-right:1px solid rgba(255,255,255,.18)}
.search{position:absolute;right:9px;top:11px;width:171px;height:17px;background:var(--white);border:1px solid #ccc;font-size:8px;color:#aaa;padding:3px 8px}
.search svg{position:absolute;right:4px;top:3px;width:9px;height:9px}

.hero{top:116px;left:84px;width:665px;height:271px;background:linear-gradient(100deg,#b9b3ab 0%,#8c8a80 38%,#4f6f5a 60%,#8fb06a 78%,#5b6b5e 100%)}
.hero-caption{position:absolute;left:18px;top:101px;width:310px;height:87px;background:rgba(90,90,90,.78);color:var(--white);padding:17px 15px}
.hero-caption h2{font-family:"PT Sans Narrow",sans-serif;font-size:11px;font-weight:700;margin-bottom:10px}
.hero-caption p{font-size:8px;line-height:17px}
.hero-btn{position:absolute;left:18px;top:186px;width:87px;height:28px;background:var(--brand);color:var(--white);font-size:10px;font-weight:700;line-height:28px;padding-left:15px}
.dots{position:absolute;left:20px;top:245px;display:flex;gap:4px}
.dots span{width:10px;height:10px;border-radius:50%;background:var(--white)}
.dots span:first-child{background:#555}

.welcome{top:410px;left:94px;width:655px;text-align:center}
.welcome h1{font-family:"PT Sans Narrow",sans-serif;font-size:11px;font-weight:700;color:var(--brand);margin-bottom:12px}
.welcome p{font-size:8px;line-height:13.7px;color:var(--body);margin-bottom:14px;text-align:justify;text-align-last:center}

.section-title{font-family:"PT Sans Narrow",sans-serif;font-size:11px;font-weight:700;color:var(--brand)}
.feature{top:594px;width:208px}
.feature .section-title{margin-bottom:14px}
.feature .photo{width:208px;height:94px}
.feature p{font-size:8px;line-height:16.6px;color:var(--muted);margin-top:8px}
.btn-small{display:inline-block;margin-top:6px;background:var(--brand);color:var(--white);font-size:8px;padding:2px 6px}

.gallery-main{top:861px;left:90px;width:263px;height:175px;border:3px solid #e8e8e8;background:linear-gradient(180deg,#4f6b55 0%,#6c8066 35%,#c7bcae 65%,#8a6a50 100%)}
.arrow{position:absolute;top:78px;width:12px;height:24px}
.thumb{width:67px;height:51px;border:3px solid #e8e8e8}
.gallery-note{top:1049px;left:90px;font-size:8px;line-height:16px;color:var(--muted)}
.post-btn{top:1048px;left:414px;width:94px;height:33px;background:var(--brand);color:var(--white);font-family:"PT Sans Narrow",sans-serif;font-weight:700;font-size:9px;display:flex;align-items:center;justify-content:center;gap:4px}
.post-btn svg{width:18px;height:15px}

.course{left:541px;display:flex;gap:22px}
.course .cover{width:65px;height:65px}
.course h3{font-size:10px;font-weight:700;color:#444;margin-top:2px}
.course .price{font-size:10px;color:var(--brand);margin-top:4px}
.course .cart{display:inline-block;margin-top:6px;background:var(--brand);color:var(--white);font-size:8px;padding:5px 5px}

.footer{top:1113px;left:0;width:831px;height:87px;background:var(--brand)}
.footer-nav{position:absolute;left:90px;top:33px;font-size:10px;color:var(--white);display:flex}
.footer-nav span{margin:0 14px}
.footer-copy{position:absolute;left:90px;top:55px;font-size:10px;color:var(--white)}
.social{position:absolute;left:662px;top:37px;display:flex;gap:5px}
.social span{width:23px;height:23px;border-radius:50%;border:2px solid rgba(255,255,255,.5)}
</style>
</head>
<body>

<div class="utility abs">
  <a href="#">Help</a> | <a href="#">Sitemap</a> |
  <svg viewBox="0 0 14 12"><path d="M1 1h2l2 7h7l1-5H4" fill="none" stroke="#444" stroke-width="1"/><circle cx="6" cy="10.5" r="1" fill="#444"/><circle cx="11" cy="10.5" r="1" fill="#444"/></svg>
  <a href="#">Add To Cart</a>
</div>

<div class="brand abs">
  <span class="brand-mark"></span>
  <div>
    <div class="brand-name">Tallowbrook Classroom Services</div>
    <div class="brand-tag">21st Century Leading Teaching Learning</div>
  </div>
</div>

<nav class="nav abs">
  <a href="#">HOME</a><a href="#">ABOUT</a><a href="#">SERVICES</a><a href="#">RESOURCES</a><a href="#">MEDIA GALLERY</a><a href="#">CONTACT</a>
  <div class="search">Search
    <svg viewBox="0 0 10 10"><circle cx="4" cy="4" r="3" fill="none" stroke="#999"/><path d="M6 6l3 3" stroke="#999"/></svg>
  </div>
</nav>

<section class="hero abs" role="img" aria-label="Smiling schoolboy holding a molecule model in a classroom with classmates">
  <div class="hero-caption">
    <h2>TALLOWBROOK CLASSROOM SERVICES</h2>
    <p>Neque porro quisquam est, qui dolorem ipsum quia dolor sit amet, consectetur, adipisci velit, sed quia non numquam eius modi</p>
  </div>
  <a class="hero-btn" href="#">Learn More</a>
  <div class="dots"><span></span><span></span><span></span><span></span></div>
</section>

<section class="welcome abs">
  <h1>WELCOME TO TALLOWBROOK CLASSROOM SERVICES</h1>
  <p>At vero eos et accusamus et iusto odio dignissimos ducimus qui blanditiis praesentium voluptatum deleniti atque corrupti quos dolores et quas molestias excepturi sint occaecati cupiditate non provident, similique sunt in culpa qui officia deserunt mollitia animi, id est laborum et dolorum fuga. Et harum quidem rerum facilis est et expedita distinctio. Nam libero tempore, cum soluta nobis est eligendi optio cumque nihil impedit quo minus id quod maxime placeat facere possimus, omnis voluptas assumenda est, omnis dolor repellendus. Temporibus autem quibusdam et aut officiis debitis aut rerum necessitatibus saepe eveniet ut et voluptates repudiandae sint et molestiae non recusandae.</p>
  <p>At vero eos et accusamus et iusto odio dignissimos ducimus qui blanditiis praesentium voluptatum deleniti atque corrupti quos dolores et quas molestias excepturi sint occaecati cupiditate non provident, similique sunt in culpa qui officia deserunt mollitia animi, id est laborum et dolorum fuga. Et harum quidem rerum facilis est et expedita distinctio. Nam libero tempore, cum soluta nobis est eligendi optio cumque nihil impedit quo minus id quod maxime placeat facere possimus, omnis voluptas assumenda est, omnis dolor repellendus. Temporibus autem quibusdam et aut officiis debitis aut rerum necessitatibus saepe eveniet ut et voluptates repudiandae sint et molestiae non recusandae.</p>
</section>

<article class="feature abs" style="left:90px">
  <h2 class="section-title">STARTING A SCHOOL</h2>
  <div class="photo" role="img" aria-label="Brick school building under a blue sky" style="background:linear-gradient(180deg,#8fb3dc 0%,#a4c0e0 25%,#8a5a45 45%,#6f4636 75%,#5d7a44 100%)"></div>
  <p>Lorem Ipsum is simply dummy text of the printing and typesetting industry. Lorem Ipsum has been the industry's standard dummy text ever since the 1500s, when an unknown printer took a galley ...</p>
  <a class="btn-small" href="#">Read More</a>
</article>

<article class="feature abs" style="left:311px">
  <h2 class="section-title">MANAGING A SCHOOL</h2>
  <div class="photo" role="img" aria-label="Teacher helping young pupils at their desks" style="background:linear-gradient(120deg,#c9a95b 0%,#d9c7a8 35%,#9a8a7c 60%,#e2cfb4 100%)"></div>
  <p>Lorem Ipsum is simply dummy text of the printing and typesetting industry. Lorem Ipsum has been the industry's standard dummy text ever since the 1500s, when an unknown printer took a galley ...</p>
  <a class="btn-small" href="#">Read More</a>
</article>

<article class="feature abs" style="left:533px">
  <h2 class="section-title">FOUNDATION MANAGEMENT</h2>
  <div class="photo" role="img" aria-label="Group of smiling adult professionals" style="background:linear-gradient(90deg,#d9c3ae 0%,#e8ddd2 30%,#8a6a52 50%,#e3d4c4 75%,#cbb39c 100%)"></div>
  <p>Lorem Ipsum is simply dummy text of the printing and typesetting industry. Lorem Ipsum has been the industry's standard dummy text ever since the 1500s, when an unknown printer took a galley ...</p>
  <a class="btn-small" href="#">Read More</a>
</article>

<h2 class="section-title abs" style="top:835px;left:90px">POST PHOTOS</h2>
<div class="gallery-main abs" role="img" aria-label="Teacher in a shirt and tie standing before a chalkboard with pupils">
  <svg class="arrow" style="left:6px" viewBox="0 0 12 24"><path d="M10 2L2 12l8 10" fill="none" stroke="var(--brand)" stroke-width="3"/></svg>
  <svg class="arrow" style="right:6px" viewBox="0 0 12 24"><path d="M2 2l8 10-8 10" fill="none" stroke="var(--brand)" stroke-width="3"/></svg>
</div>
<div class="thumb abs" style="top:861px;left:367px;background:linear-gradient(135deg,#7f9aa8,#d8dde0)" role="img" aria-label="Teacher at a whiteboard"></div>
<div class="thumb abs" style="top:861px;left:441px;background:linear-gradient(135deg,#d6a066,#8c6a4a)" role="img" aria-label="Pupils working together"></div>
<div class="thumb abs" style="top:922px;left:367px;background:linear-gradient(135deg,#3f6b50,#b07a5e)" role="img" aria-label="Teacher with a small class"></div>
<div class="thumb abs" style="top:922px;left:441px;background:linear-gradient(135deg,#5c7a5a,#c8b5a0)" role="img" aria-label="Teacher at a desk"></div>
<div class="thumb abs" style="top:983px;left:367px;background:linear-gradient(135deg,#c89d80,#e4d4c8)" role="img" aria-label="Pupils reading together"></div>
<div class="thumb abs" style="top:983px;left:441px;background:linear-gradient(135deg,#e0e4e0,#3d6a45)" role="img" aria-label="Teacher writing on a green board"></div>
<p class="gallery-note abs">Lorem Ipsum is simply dummy text of the printing and typesetting industry.<br>Lorem Ipsum has been the industry's standard dummy text ever since the 1500s</p>
<a class="post-btn abs" href="#">
  <svg viewBox="0 0 18 15"><rect x="1" y="3" width="13" height="10" fill="none" stroke="#fff" stroke-width="1.2"/><rect x="4" y="1" width="13" height="10" fill="none" stroke="#fff" stroke-width="1.2"/><path d="M5 10l3-3 3 3 2-2 3 3" fill="none" stroke="#fff"/></svg>
  POST A PHOTO
</a>

<h2 class="section-title abs" style="top:835px;left:533px">OUR COURSES</h2>
<div class="course abs" style="top:860px">
  <div class="cover" role="img" aria-label="Red course book cover" style="background:linear-gradient(160deg,#2a5aa8 0%,#c81e2e 55%,#8c0f1c 100%)"></div>
  <div><h3>Sed ut perspiciatis unde</h3><div class="price">$ 45.00</div><a class="cart" href="#">ADD TO CART</a></div>
</div>
<div class="course abs" style="top:936px">
  <div class="cover" role="img" aria-label="Grey and blue course book cover" style="background:linear-gradient(180deg,#c9d2da 0%,#6f8aa5 50%,#d6dade 100%)"></div>
  <div><h3>Sed ut perspiciatis unde</h3><div class="price">$ 45.00</div><a class="cart" href="#">ADD TO CART</a></div>
</div>
<div class="course abs" style="top:1014px">
  <div class="cover" role="img" aria-label="Brown and gold course book cover" style="background:linear-gradient(180deg,#4a3520 0%,#c98a2e 45%,#6b4424 100%)"></div>
  <div><h3>Sed ut perspiciatis unde</h3><div class="price">$ 45.00</div><a class="cart" href="#">ADD TO CART</a></div>
</div>

<footer class="footer abs">
  <div class="footer-nav">
    <a href="#">Home</a><span>|</span><a href="#">About</a><span>|</span><a href="#">Services</a><span>|</span><a href="#">Resources</a><span>|</span><a href="#">Media Gallery</a><span style="margin:0 18px 0 24px">|</span><a href="#">Contact</a>
  </div>
  <div class="footer-copy">Copyright ©2013 Company Name &nbsp; - All rights reserved</div>
  <div class="social">
    <span style="background:#5fb7e6" aria-label="Quipline"></span>
    <span style="background:#3d64b0" aria-label="Chatterleaf"></span>
    <span style="background:#f3a73a" aria-label="Blog"></span>
  </div>
</footer>

</body>
</html>
```